Lead Sales Portal Needs to Generate B2B Signup's

We are looking for banner ad designs to drive new business (B2B) traffic to our insurance and mortgage industry self serve lead sites. The sites are HomeLoanProspectHub.com and CoverageProspectHub.com, and we service over 45,000 insurance agents and mortgage lenders in a self serve lead portal model. We want our banners to generate more of these clients.

Our clients come to our sites, browse our database and then pick out and purchase the consumer leads that they need to generate new business.

We advertise extensively on Zorvix and on other PPC platforms, and our existing banners are looking really tired.

Some of the ad copy that works well for us is:

Cherry Pick Your Life Leads - Why Pay More Than $3.50 For Life Insurance Leads?
Sign up today and we'll match up to $250

Agents - Here's $250 For New Clients. Cherry Pick Your Life Insurance Leads & Save! Sign up today and we'll match up to $250

One of our Landing Pages that performs well is here:
http://www.coverageprospecthub.com/lp/008/

One of our competitors ad's are here:

http://www.tralvo.com/search/results?q=PolicyBeacon&ad=427360

We're looking for a design that is eye catching, uses our "Deeply Discounted Leads" and our "$250 match bonus"

This is the second contest that we have for the same sites. The previous designs were great and really performed well, so we are looking for new designs now that 6 months have passed. I have uploaded some winning banners from the last group for your information.
Updates

Project Deadline Extended
Reason: I've been asked by some of the designers to delay a day to get their designs in. I'm happy to do it!

Target Market(s)

These are insurance agents and mortgage lenders. All of our clients are business' or individuals within the business. This is a B2B campaign, so we need something that is professional and upscale. These are NOT consumer facing ad's!

Industry/Entity Type

Insurance

Font styles to use
Sans Serif

Requirements
Must have
• We must have the logos for the sites in the banners. Also, we must have a call to action arrow and "Go" button. Some animation is necessary, (especially around the arrow and the GO button).

One or two designs.

File type

.JPEG
.JPG
.PNG
.GIF

File size

150 KB or smaller

Image sizes

Vertical rectangle: 240 x 400
Mobile leaderboard: 320 x 50
Banner: 468 x 60
Leaderboard: 728 x 90
Square: 250 x 250
Small square: 200 x 200
Large rectangle: 336 x 280
Inline rectangle: 300 x 250
Skyscraper: 120 x 600
Wide skyscraper: 160 x 600
Half-page: 300 x 600
Large leaderboard: 970 x 90

```html
<!DOCTYPE html>
<html lang="en">
<head>
<meta charset="utf-8">
<title>Coverage Prospect Hub – Agent Signup Banner Set</title>
<link rel="stylesheet" href="https://fonts.googleapis.com/css2?family=Roboto:wght@300;400;700&display=swap">
<style>
  :root{
    --stage:#6a6a6a;
    --green:#8cc63f;
    --green-dark:#5f9a22;
    --green-light:#b2e052;
    --black:#0e0e0e;
    --white:#ffffff;
    --ink:#2a2a2a;
    --photo-a:#f1efec;
    --photo-b:#c9b7a2;
  }
  *{box-sizing:border-box;margin:0;padding:0}
  html,body{width:1200px;height:843px;overflow:hidden}
  body{background:var(--stage);font-family:"Roboto",Arial,sans-serif;position:relative}

  .banner{position:absolute;overflow:hidden;display:flex;background:var(--black);box-shadow:0 2px 6px rgba(0,0,0,.45)}

  .agents{color:var(--green);font-weight:700;line-height:1;letter-spacing:-.01em;white-space:nowrap}
  .offer{font-weight:700;text-transform:uppercase;line-height:1.05;white-space:nowrap}
  .pitch{color:var(--white);font-weight:700;text-transform:uppercase;line-height:1.15;text-align:center;white-space:nowrap}
  .match{font-weight:300;line-height:1.2;text-align:center;white-space:nowrap}
  .photo{background:linear-gradient(100deg,var(--photo-a) 0%,var(--photo-a) 35%,var(--photo-b) 70%,#9b8064 100%)}

  .brand{display:inline-flex;align-items:center;gap:.35em;color:var(--white);font-weight:300;white-space:nowrap}
  .brand-dot{width:1.2em;height:1.2em;border-radius:50%;background:var(--white);flex:none}

  .go{display:inline-flex;align-items:center;gap:.35em;padding:.08em .35em .08em .6em;border-radius:1em;
      background:linear-gradient(var(--green-light),var(--green-dark));color:var(--white);font-weight:700;line-height:1.1;
      box-shadow:0 0 0 .06em rgba(255,255,255,.25) inset}
  .go-dot{width:.6em;height:.6em;border-radius:50%;background:var(--white);display:inline-flex;align-items:center;justify-content:center}
  .go-dot svg{width:.4em;height:.4em}
  .cta-arrow{width:1.6em;height:1.6em;flex:none}
  .action{display:flex;align-items:center;justify-content:center;gap:.5em}

  /* square family */
  .square{flex-direction:column}
  .square .top{height:52%;background:var(--white);display:flex}
  .square .head{flex:1;display:flex;flex-direction:column;justify-content:center;align-items:center;text-align:center;padding-left:.5em}
  .square .agents{font-size:2.9em}
  .square .offer{color:var(--ink);font-size:1.65em}
  .square .photo{width:40%}
  .square .bottom{flex:1;border-top:.3em solid var(--green);display:flex;flex-direction:column;align-items:center;justify-content:center;gap:.35em}
  .square .pitch{font-size:1.75em}
  .square .match{color:var(--white);font-size:1.35em}
  .square .brand{font-size:1.3em}
  .square .go{font-size:1.8em}

  /* vertical family */
  .tower{flex-direction:column}
  .tower .head{display:flex;flex-direction:column;align-items:center;justify-content:center;text-align:center}
  .tower .agents{font-size:2.9em}
  .tower .offer{color:var(--white);font-size:1.75em}
  .tower .photo{border-bottom:.25em solid var(--green)}
  .tower .bottom{flex:1;display:flex;flex-direction:column;align-items:center;justify-content:center;gap:.45em;padding:0 .2em}
  .tower .pitch{font-size:1.75em;font-weight:400}
  .tower .match{color:var(--green);font-size:1.5em;font-weight:400}
  .tower .go{font-size:1.9em}
  .tower .brand{font-size:1.4em}

  /* wide family */
  .wide .left{background:var(--white);display:flex;border-right:.3em solid var(--green)}
  .wide .head{flex:1;display:flex;flex-direction:column;justify-content:center;align-items:center;text-align:center}
  .wide .agents{font-size:2.9em}
  .wide .offer{color:var(--ink);font-size:1.65em}
  .wide .photo{width:42%}
  .wide .right,.mobile .right{flex:1;display:flex;align-items:center;justify-content:space-between;gap:.6em;padding:0 .8em}
  .copy{display:flex;flex-direction:column;align-items:center;flex:1}
  .copy .pitch{font-size:1.6em}
  .copy .match{color:var(--green);font-size:1.4em;font-weight:400}
  .side{display:flex;flex-direction:column;align-items:center;gap:.35em;flex:none}
  .side .brand{font-size:1.3em}
  .side .go{font-size:1.7em}
</style>
</head>
<body>

<svg width="0" height="0" style="position:absolute">
  <defs>
    <symbol id="curl" viewBox="0 0 24 24"><path d="M20 2C21 11 15 17 5 17M5 17l5-4.5M5 17l5.5 3.5" fill="none" stroke="#fff" stroke-width="1.8" stroke-linecap="round" stroke-linejoin="round"/></symbol>
    <symbol id="flat" viewBox="0 0 24 24"><path d="M2 18C8 18 16 15 21 8M21 8l-5 1M21 8l-.5 5" fill="none" stroke="#fff" stroke-width="1.8" stroke-linecap="round" stroke-linejoin="round"/></symbol>
    <symbol id="tri" viewBox="0 0 10 10"><path d="M2 1l6 4-6 4z" fill="#5f9a22"/></symbol>
  </defs>
</svg>

<!-- Square 250 -->
<section class="banner square" style="left:52px;top:50px;width:278px;height:231px;font-size:10px">
  <div class="top"><div class="head"><p class="agents">AGENTS!</p><p class="offer">Here's $250 for<br>new clients</p></div><div class="photo" role="img" aria-label="Portrait photo of a smiling young professional woman"></div></div>
  <div class="bottom"><p class="pitch">Cherry pick your life<br>insurance leads &amp; save!</p><p class="match">Sign up today and we'll match up to $250</p>
    <div class="action"><span class="brand"><span class="brand-dot"></span>Coverage Prospect Hub</span><span class="go">GO<span class="go-dot"><svg><use href="#tri"/></svg></span></span><svg class="cta-arrow"><use href="#curl"/></svg></div></div>
</section>

<!-- Large leaderboard -->
<section class="banner wide" style="left:346px;top:47px;width:800px;height:74px;font-size:9.5px">
  <div class="left" style="width:42.5%"><div class="head"><p class="agents">AGENTS!</p><p class="offer">Here's $250 for<br>new clients</p></div><div class="photo" role="img" aria-label="Portrait photo of a smiling young professional woman"></div></div>
  <div class="right"><div class="copy"><p class="pitch" style="font-size:1.95em">Cherry pick your life<br>insurance leads &amp; save!</p><p class="match" style="font-size:1.85em">Sign up today and we'll match up to $250</p></div>
    <svg class="cta-arrow" style="font-size:14px;align-self:flex-end;margin-bottom:6px"><use href="#flat"/></svg>
    <div class="side"><span class="brand" style="font-size:1.75em"><span class="brand-dot"></span>Coverage Prospect Hub</span><span class="go" style="font-size:1.95em">GO<span class="go-dot"><svg><use href="#tri"/></svg></span></span></div></div>
</section>

<!-- Small square -->
<section class="banner square" style="left:388px;top:165px;width:154px;height:154px;font-size:5.6px">
  <div class="top"><div class="head"><p class="agents">AGENTS!</p><p class="offer">Here's $250 for<br>new clients</p></div><div class="photo" role="img" aria-label="Portrait photo of a smiling young professional woman"></div></div>
  <div class="bottom"><p class="pitch">Cherry pick your life<br>insurance leads &amp; save!</p><p class="match">Sign up today and we'll match up to $250</p>
    <div class="action"><span class="brand"><span class="brand-dot"></span>Coverage Prospect Hub</span><span class="go">GO<span class="go-dot"><svg><use href="#tri"/></svg></span></span><svg class="cta-arrow"><use href="#curl"/></svg></div></div>
</section>

<!-- Leaderboard -->
<section class="banner wide" style="left:594px;top:147px;width:550px;height:68px;font-size:8.3px">
  <div class="left" style="width:41%"><div class="head"><p class="agents">AGENTS!</p><p class="offer">Here's $250 for<br>new clients</p></div><div class="photo" role="img" aria-label="Portrait photo of a smiling young professional woman"></div></div>
  <div class="right" style="padding:0 .6em;gap:.3em"><div class="copy"><p class="pitch" style="font-size:1.55em">Cherry pick your life<br>insurance leads &amp; save!</p><p class="match" style="font-size:1.3em">Sign up today and we'll match up to $250</p></div>
    <div class="side"><span class="brand" style="font-size:1.2em"><span class="brand-dot"></span>Coverage Prospect Hub</span><span class="action" style="gap:.3em"><span class="go" style="font-size:1.6em">GO<span class="go-dot"><svg><use href="#tri"/></svg></span></span><svg class="cta-arrow"><use href="#flat"/></svg></span></div></div>
</section>

<!-- Inline rectangle -->
<section class="banner square" style="left:52px;top:321px;width:229px;height:189px;font-size:8.2px">
  <div class="top"><div class="head"><p class="agents">AGENTS!</p><p class="offer">Here's $250 for<br>new clients</p></div><div class="photo" role="img" aria-label="Portrait photo of a smiling young professional woman"></div></div>
  <div class="bottom"><p class="pitch">Cherry pick your life<br>insurance leads &amp; save!</p><p class="match">Sign up today and we'll match up to $250</p>
    <div class="action"><span class="brand"><span class="brand-dot"></span>Coverage Prospect Hub</span><span class="go">GO<span class="go-dot"><svg><use href="#tri"/></svg></span></span><svg class="cta-arrow"><use href="#curl"/></svg></div></div>
</section>

<!-- Large square -->
<section class="banner square" style="left:166px;top:563px;width:186px;height:184px;font-size:6.7px">
  <div class="top"><div class="head"><p class="agents">AGENTS!</p><p class="offer">Here's $250 for<br>new clients</p></div><div class="photo" role="img" aria-label="Portrait photo of a smiling young professional woman"></div></div>
  <div class="bottom"><p class="pitch">Cherry pick your life<br>insurance leads &amp; save!</p><p class="match">Sign up today and we'll match up to $250</p>
    <div class="action"><span class="brand"><span class="brand-dot"></span>Coverage Prospect Hub</span><span class="go">GO<span class="go-dot"><svg><use href="#tri"/></svg></span></span><svg class="cta-arrow"><use href="#curl"/></svg></div></div>
</section>

<!-- Vertical rectangle -->
<section class="banner tower" style="left:388px;top:373px;width:205px;height:340px;font-size:10.5px">
  <div class="head" style="height:28%"><p class="agents">AGENTS!</p><p class="offer">Here's $250 for<br>new clients</p></div>
  <div class="photo" role="img" aria-label="Portrait photo of a smiling young professional woman in a bright office" style="height:32%"></div>
  <div class="bottom"><p class="pitch" style="font-size:1.42em">Cherry pick your life<br>insurance leads &amp; save!</p><p class="match">Sign up today and we'll<br>match up to $250</p>
    <div class="action"><span class="go">GO<span class="go-dot"><svg><use href="#tri"/></svg></span></span><svg class="cta-arrow"><use href="#curl"/></svg></div></div>
</section>

<!-- Half page -->
<section class="banner tower" style="left:630px;top:281px;width:218px;height:432px;font-size:12.5px">
  <div class="head" style="height:23%"><p class="agents">AGENTS!</p><p class="offer">Here's $250 for<br>new clients</p></div>
  <div class="photo" role="img" aria-label="Portrait photo of a smiling young professional woman in a bright office" style="height:30%"></div>
  <div class="bottom"><p class="pitch">Cherry pick your<br>life insurance<br>leads &amp; save!</p><p class="match">Sign up today and we'll<br>match up to $250</p>
    <div class="action"><span class="go">GO<span class="go-dot"><svg><use href="#tri"/></svg></span></span><svg class="cta-arrow"><use href="#curl"/></svg></div>
    <span class="brand" style="font-size:1.25em"><span class="brand-dot"></span>Coverage Prospect Hub</span></div>
</section>

<!-- Wide skyscraper -->
<section class="banner tower" style="left:886px;top:250px;width:125px;height:463px;font-size:9px">
  <div class="head" style="height:21%"><p class="agents">AGENTS!</p><p class="offer">Here's $250<br>for new<br>clients</p></div>
  <div class="photo" role="img" aria-label="Portrait photo of a smiling young professional woman" style="height:26%"></div>
  <div class="bottom"><p class="pitch">Cherry pick<br>your life<br>insurance<br>leads &amp; save!</p><p class="match">Sign up today<br>and we'll match<br>up to $250</p>
    <div class="action"><span class="go">GO<span class="go-dot"><svg><use href="#tri"/></svg></span></span></div>
    <span class="brand" style="font-size:1.05em"><span class="brand-dot"></span>Coverage Prospect Hub</span></div>
</section>

<!-- Skyscraper -->
<section class="banner tower" style="left:1053px;top:250px;width:93px;height:463px;font-size:7px">
  <div class="head" style="height:22%"><p class="agents">AGENTS!</p><p class="offer">Here's $250<br>for new<br>clients</p></div>
  <div class="photo" role="img" aria-label="Portrait photo of a smiling young professional woman" style="height:25%"></div>
  <div class="bottom"><p class="pitch">Cherry pick<br>your life<br>insurance<br>leads &amp; save!</p><p class="match">Sign up today<br>and we'll match<br>up to $250</p>
    <div class="action"><span class="go">GO<span class="go-dot"><svg><use href="#tri"/></svg></span></span></div>
    <span class="brand" style="font-size:.95em"><span class="brand-dot"></span>Coverage Prospect Hub</span></div>
</section>

<!-- Banner 468 -->
<section class="banner wide" style="left:452px;top:747px;width:359px;height:47px;font-size:5.4px">
  <div class="left" style="width:41%"><div class="head"><p class="agents">AGENTS!</p><p class="offer">Here's $250 for<br>new clients</p></div><div class="photo" role="img" aria-label="Portrait photo of a smiling young professional woman"></div></div>
  <div class="right" style="padding:0 .6em;gap:.4em"><div class="copy"><p class="pitch" style="font-size:1.55em">Cherry pick your life<br>insurance leads &amp; save!</p><p class="match" style="font-size:1.3em">Sign up today and we'll match up to $250</p></div>
    <div class="side"><span class="brand" style="font-size:1.1em"><span class="brand-dot"></span>Coverage Prospect Hub</span><span class="go" style="font-size:1.6em">GO<span class="go-dot"><svg><use href="#tri"/></svg></span></span></div></div>
</section>

<!-- Mobile leaderboard -->
<section class="banner mobile" style="left:842px;top:747px;width:278px;height:44px;font-size:5.6px">
  <div class="right" style="gap:.4em"><div class="copy"><p class="pitch" style="font-size:1.6em">Cherry pick your life<br>insurance leads &amp; save!</p><p class="match" style="color:var(--green);font-size:1.45em">Sign up today and we'll match up to $250</p></div>
    <svg class="cta-arrow" style="align-self:flex-end;margin-bottom:4px"><use href="#flat"/></svg>
    <div class="side"><span class="brand" style="font-size:1.25em"><span class="brand-dot"></span>Coverage Prospect Hub</span><span class="go" style="font-size:1.8em">GO<span class="go-dot"><svg><use href="#tri"/></svg></span></span></div></div>
</section>

</body>
</html>
```